Einladungskarten-Design für Schützenverein
super gute Zusammenarbeit. Werde für weitere Arbeiten gerne darauf zurückkommen.
Zielgruppe
Wir sind ein Schützenverein und möchten mit einem neuzeitlichen Design für unser traditionelles Grümpelschiessen Werbung machen und die jüngere Generation für diesen schönen Sport begeistern.

```html
<!DOCTYPE html>
<html lang="de">
<head>
<meta charset="utf-8">
<title>Einladung zum Grümpelschiessen 2021</title>
<link href="https://fonts.googleapis.com/css2?family=Montserrat:wght@800&family=Lato:ital,wght@0,400;0,700;0,900;1,700&display=swap" rel="stylesheet">
<style>
  :root {
    --navy: #1f2a7a;
    --yellow: #f0c800;
    --white: #f4f4f6;
    --grass: #4f8a2a;
    --grass-dark: #2f6a1a;
    --bg: #e6e6e6;
  }
  * { margin: 0; padding: 0; box-sizing: border-box; }
  html, body { width: 1200px; height: 800px; overflow: hidden; background: var(--bg); }
  body { display: flex; align-items: center; justify-content: center; font-family: "Lato", sans-serif; }

  .flyer {
    position: relative; width: 540px; height: 764px; overflow: hidden;
    background: linear-gradient(135deg, var(--grass), var(--grass-dark));
    box-shadow: 0 12px 30px rgba(0,0,0,.25);
  }
  .hero-photo {
    position: absolute; left: 0; top: 0; width: 100%; height: 300px;
    background: linear-gradient(100deg, #3e5a22 0%, #7f9a3a 45%, #c8c040 80%, #e6cf3a 100%);
  }
  .title-band {
    position: absolute; left: 0; top: 276px; width: 100%; height: 100px;
    background: var(--navy);
  }
  .title {
    position: absolute; left: 24px; top: 298px; width: 290px;
    font-family: "Montserrat", sans-serif; font-weight: 800; line-height: 1.2;
    white-space: nowrap;
  }
  .title .line1 { display: block; color: #fff; font-size: 25px; }
  .title .line2 { display: block; color: var(--yellow); font-size: 20px; }

  .year-box {
    position: absolute; left: 326px; top: 250px; width: 116px; height: 150px;
    background: var(--yellow); display: flex; align-items: center; justify-content: center;
  }
  .year-box .frame {
    width: 98px; height: 132px; border: 3px solid #fff;
    display: flex; flex-direction: column; align-items: center; justify-content: center;
    font-family: "Montserrat", sans-serif; font-weight: 800; font-size: 48px; line-height: 1; color: #fff;
  }

  .club-mark {
    position: absolute; left: 452px; top: 292px; width: 78px; height: 100px;
    background: #fff; display: flex; flex-direction: column; align-items: center; justify-content: center; gap: 8px;
    color: var(--navy); font-weight: 900; font-size: 10px; text-align: center; line-height: 1.2; padding: 6px;
  }
  .club-mark .square { width: 22px; height: 22px; background: var(--yellow); }

  .info-panel {
    position: absolute; left: 30px; top: 376px; width: 480px; height: 290px;
    background: var(--white); color: var(--navy);
  }
  .when { position: absolute; left: 0; top: 14px; width: 184px; text-align: right; }
  .when .day { font-size: 40px; font-weight: 700; line-height: 1; }
  .when .date { font-size: 19px; font-weight: 700; margin-top: 2px; }
  .when .time { font-size: 19px; font-weight: 700; margin-top: 16px; line-height: 1.15; }

  .divider { position: absolute; left: 196px; top: 16px; width: 3px; height: 220px; background: var(--navy); }

  .details { position: absolute; left: 212px; top: 16px; width: 262px; font-size: 14.5px; line-height: 1.22; }
  .details h3 { font-size: 15px; font-weight: 900; }
  .details p { margin-bottom: 8px; }

  .shooter-figures {
    position: absolute; left: 12px; top: 170px; width: 172px; height: 80px;
    background: linear-gradient(180deg, rgba(31,42,122,.15), rgba(31,42,122,.55));
  }

  .footer-band {
    position: absolute; left: 0; top: 652px; width: 100%; height: 112px; background: var(--navy);
  }
  .footer-text {
    position: absolute; left: 20px; top: 664px; width: 500px; text-align: center;
    color: #fff; font-weight: 700; font-style: italic; font-size: 17px; line-height: 1.3;
  }
  .footer-strip { position: absolute; left: 0; top: 748px; width: 100%; height: 16px; background: var(--yellow); }
  .url-tab {
    position: absolute; left: 120px; top: 722px; width: 260px; height: 42px;
    background: var(--yellow); clip-path: polygon(8% 0, 92% 0, 100% 100%, 0 100%);
    display: flex; align-items: center; justify-content: center;
    color: var(--navy); font-weight: 900; font-size: 19px;
  }
</style>
</head>
<body>
  <article class="flyer">
    <div class="hero-photo" role="img" aria-label="Foto: Schützin liegt mit Gewehr im Gras am Waldrand"></div>

    <div class="title-band"></div>
    <h1 class="title">
      <span class="line1">EINLADUNG ZUM</span>
      <span class="line2">GRÜMPELSCHIESSEN</span>
    </h1>

    <div class="year-box"><div class="frame"><span>20</span><span>21</span></div></div>

    <div class="club-mark">
      <span class="square"></span>
      <span>Schützenverein Talbach</span>
    </div>

    <section class="info-panel">
      <div class="when">
        <div class="day">Sonntag</div>
        <div class="date">29. August</div>
        <div class="time">08.00 - 12.00<br>Uhr durchgehend</div>
      </div>
      <div class="shooter-figures" role="img" aria-label="Silhouetten zweier liegender Schützen mit Gewehren"></div>
      <div class="divider"></div>
      <div class="details">
        <h3>Wo :</h3>
        <p>BEIM SCHÜTZENHAUS TALBACH (Parkplätze bei der Talstation der Sonnalpbahn)</p>
        <h3>Wer :</h3>
        <p>Einzel, Paare und Familien &gt; einfach jedermann ob jung ob alt aus nah und fern, Frau und Mann</p>
        <h3>Unser Angebot :</h3>
        <p>Grümpelstich und Festwirtschaft mit Mittags -menü in herrlicher Umgebung</p>
      </div>
    </section>

    <div class="footer-band"></div>
    <p class="footer-text">Wir laden Sie herzlich zu einem gemütlichen Sonntag ein und freuen uns auf Ihren Besuch und Ihre Teilnahme.</p>
    <div class="footer-strip"></div>
    <div class="url-tab">www.svtalbach.ch</div>
  </article>
</body>
</html>
```